Stationery for Public Accountant Practice

Name of Practice
Holloway Advisory Pty Ltd
Tel: 0417262938
Postal Address : PO Box 482, Elmsford Park, Vic 3187

Target Market(s)

Small Business Clients

Industry/Entity Type

Accounting

Font styles to use
Serif

Requirements
Must have
• Letterhead, business card, With compliments slip
Nice to have
• Conservative

```html
<!DOCTYPE html>
<html lang="en">
<head>
<meta charset="utf-8">
<title>Holloway Advisory Pty Ltd — Stationery</title>
<link rel="stylesheet" href="https://fonts.googleapis.com/css2?family=Lato:ital,wght@0,400;0,700;1,400;1,700&family=Tinos:wght@400&display=swap">
<style>
:root{
  --blue:#1a6fc4;
  --blue-deep:#0f56aa;
  --blue-light:#2e86d4;
  --ink:#1d1d1d;
  --paper:#ffffff;
  --stage-top:#e7e9ec;
  --stage-mid:#e6e6e6;
  --stage-dark:#2f2f30;
  --rule-dark:#141414;
}
*{margin:0;padding:0;box-sizing:border-box}
html,body{width:1200px;height:2894px;overflow:hidden}
body{position:relative;font-family:"Lato",Arial,sans-serif;color:var(--ink)}
.stage{position:absolute;left:0;width:1200px}
.stage--overview{top:0;height:900px;background:var(--stage-top)}
.stage--flat{top:900px;height:1110px;background:var(--stage-mid)}
.stage--cards{top:2010px;height:884px;background:var(--stage-dark)}
.piece{position:absolute;background:var(--paper);box-shadow:0 3px 10px rgba(0,0,0,.18);overflow:hidden}
.scaled{position:absolute;transform-origin:0 0}

/* brand lockup */
.brand{position:absolute;display:flex;align-items:center;gap:10px;color:var(--blue);font-weight:700;line-height:1}
.brand--white{color:#fff}
.brand-mark{width:34px;height:34px;background:currentColor;flex:none}
.brand-name{display:flex;flex-direction:column;gap:4px}
.brand-name .line1{font-size:28px;letter-spacing:.5px}
.brand-name .line2{font-size:15px;letter-spacing:3px}

/* footer strip */
.footer-contact{position:absolute;right:14px;font-size:10px;color:#444;white-space:nowrap}
.footer-contact b{color:var(--blue);font-weight:400}
.footer-bar{position:absolute;left:0;right:0;height:8px;background:var(--blue)}
.footer-bar::before{content:"";position:absolute;left:0;top:-2px;width:56%;height:6px;background:var(--rule-dark)}

/* compliments slip */
.slip{width:524px;height:256px}
.slip .brand{left:24px;top:36px}
.slip-title{position:absolute;right:22px;top:52px;font-size:19px;font-weight:700;font-style:italic}
.slip .footer-contact{bottom:20px}
.slip .footer-bar{bottom:4px}

/* envelope */
.envelope{width:520px;height:260px}
.envelope-flap{position:absolute;left:0;top:0;width:100%;height:110px}
.envelope .brand{left:50%;top:26px;transform:translateX(-50%)}

/* folder */
.folder{width:534px;height:724px;background:var(--blue-deep)}
.folder-art{position:absolute;inset:0;background:linear-gradient(160deg,var(--blue-light) 0%,var(--blue) 45%,var(--blue-deep) 100%)}
.folder .brand{left:50%;top:50%;transform:translate(-50%,-50%)}
.folder .brand-mark{width:40px;height:40px}
.folder .brand-name .line1{font-size:34px}
.folder .brand-name .line2{font-size:18px}

/* letterhead */
.letterhead{width:486px;height:690px}
.letterhead .brand{left:50%;top:22px;transform:translateX(-50%)}
.letter-body{position:absolute;left:52px;top:102px;width:384px;font-family:"Tinos","Times New Roman",serif;font-size:9.6px;line-height:1.3;color:#222}
.letter-body p{margin-bottom:9px}
.letterhead .footer-contact{bottom:22px}
.letterhead .footer-bar{bottom:6px}

/* cd */
.cd-sleeve{width:240px;height:240px;background:linear-gradient(160deg,var(--blue-light),var(--blue-deep))}
.cd-sleeve .brand{left:30px;top:64px;transform:scale(.55);transform-origin:0 0}
.cd-disc{position:absolute;width:200px;height:200px;border-radius:50%;background:#fafafa;box-shadow:0 3px 10px rgba(0,0,0,.25)}
.cd-disc::before{content:"";position:absolute;left:70px;top:70px;width:60px;height:60px;border-radius:50%;background:#d8dadd;border:8px solid #eceef0}
.cd-disc .brand{left:92px;top:30px;transform:scale(.32);transform-origin:0 0}

/* business cards */
.card{width:600px;height:340px}
.card--back{background:var(--blue-deep)}
.card--back .folder-art{background:linear-gradient(150deg,var(--blue-deep) 0%,var(--blue) 50%,var(--blue-light) 100%)}
.card--back .brand{left:50%;top:50%;transform:translate(-50%,-50%)}
.card--front .brand{right:36px;top:40px}
.card-person{position:absolute;left:40px;top:150px}
.card-name{font-size:27px;font-weight:700;font-style:italic;color:var(--blue)}
.card-role{font-size:19px;color:var(--ink);margin-top:2px}
.card-contact{position:absolute;left:40px;bottom:34px;font-size:19px;line-height:1.45}
.card-contact b{color:var(--blue);font-weight:400;font-style:italic}
</style>
</head>
<body>

<section class="stage stage--overview" aria-label="Stationery set overview">
  <div class="scaled" style="left:240px;top:24px;transform:scale(.58)">
    <div class="piece envelope" style="position:relative">
      <svg class="envelope-flap" viewBox="0 0 520 110" preserveAspectRatio="none"><path d="M0 0H520V70Q260 120 0 70Z" fill="var(--blue)"/></svg>
      <div class="brand brand--white"><span class="brand-mark"></span><span class="brand-name"><span class="line1">HOLLOWAY</span><span class="line2">ADVISORY PTY LTD</span></span></div>
    </div>
  </div>

  <div class="scaled" style="left:186px;top:286px;transform:scale(.2)">
    <div class="piece card card--back" style="position:relative">
      <div class="folder-art"></div>
      <div class="brand brand--white"><span class="brand-mark"></span><span class="brand-name"><span class="line1">HOLLOWAY</span><span class="line2">ADVISORY PTY LTD</span></span></div>
    </div>
  </div>
  <div class="scaled" style="left:300px;top:306px;transform:scale(.2)">
    <div class="piece card card--front" style="position:relative">
      <div class="brand"><span class="brand-mark"></span><span class="brand-name"><span class="line1">HOLLOWAY</span><span class="line2">ADVISORY PTY LTD</span></span></div>
      <div class="card-person"><div class="card-name">Peter Lawson</div><div class="card-role">Manager</div></div>
      <div class="card-contact"><div><b>Tel :</b> 0417262938</div><div><b>Address :</b> PO Box 482, Elmsford Park, Vic 3187</div></div>
    </div>
  </div>

  <div class="scaled" style="left:210px;top:410px;transform:scale(.67)">
    <div class="piece slip" style="position:relative">
      <div class="brand"><span class="brand-mark"></span><span class="brand-name"><span class="line1">HOLLOWAY</span><span class="line2">ADVISORY PTY LTD</span></span></div>
      <div class="slip-title">With Compliments</div>
      <div class="footer-contact"><b>Tel :</b> 0417262938 | <b>Address :</b> PO Box 482, Elmsford Park, Vic 3187</div>
      <div class="footer-bar"></div>
    </div>
  </div>

  <div class="scaled" style="left:460px;top:60px;transform:scale(.6)">
    <div class="piece folder" style="position:relative">
      <div class="folder-art" role="img" aria-label="Large soft decorative letterform in blue tones"></div>
      <div class="brand brand--white"><span class="brand-mark"></span><span class="brand-name"><span class="line1">HOLLOWAY</span><span class="line2">ADVISORY PTY LTD</span></span></div>
    </div>
  </div>

  <div class="scaled" style="left:640px;top:30px;transform:scale(.74)">
    <div class="piece letterhead" style="position:relative">
      <div class="brand"><span class="brand-mark"></span><span class="brand-name"><span class="line1">HOLLOWAY</span><span class="line2">ADVISORY PTY LTD</span></span></div>
      <div class="letter-body">
        <p>May 30, 2024</p>
        <p>Marian Tolley<br>14 Garnet Street<br>Elmsford Park, Vic 3187</p>
        <p>Dear Ms. Tolley:</p>
        <p>Thank you for choosing our practice to look after your business accounts this year.</p>
        <p>We have reviewed the records you supplied and prepared a summary of your quarterly activity statements, along with a plan for the coming financial year.</p>
        <p>Regards,</p>
        <p>Dana Whitfield</p>
      </div>
      <div class="footer-contact"><b>Tel :</b> 0417262938 | <b>Address :</b> PO Box 482, Elmsford Park, Vic 3187</div>
      <div class="footer-bar"></div>
    </div>
  </div>

  <div class="piece cd-sleeve" style="left:600px;top:570px">
    <div class="brand brand--white"><span class="brand-mark"></span><span class="brand-name"><span class="line1">HOLLOWAY</span><span class="line2">ADVISORY PTY LTD</span></span></div>
  </div>
  <div class="cd-disc" style="left:740px;top:620px">
    <div class="brand"><span class="brand-mark"></span><span class="brand-name"><span class="line1">HOLLOWAY</span><span class="line2">ADVISORY PTY LTD</span></span></div>
  </div>
</section>

<section class="stage stage--flat" aria-label="Flat stationery pieces">
  <div class="piece slip" style="left:40px;top:60px">
    <div class="brand"><span class="brand-mark"></span><span class="brand-name"><span class="line1">HOLLOWAY</span><span class="line2">ADVISORY PTY LTD</span></span></div>
    <div class="slip-title">With Compliments</div>
    <div class="footer-contact"><b>Tel :</b> 0417262938 | <b>Address :</b> PO Box 482, Elmsford Park, Vic 3187</div>
    <div class="footer-bar"></div>
  </div>

  <div class="piece envelope" style="left:640px;top:60px">
    <svg class="envelope-flap" viewBox="0 0 520 110" preserveAspectRatio="none"><path d="M0 0H520V70Q260 120 0 70Z" fill="var(--blue)"/></svg>
    <div class="brand brand--white"><span class="brand-mark"></span><span class="brand-name"><span class="line1">HOLLOWAY</span><span class="line2">ADVISORY PTY LTD</span></span></div>
  </div>

  <div class="piece folder" style="left:44px;top:376px">
    <div class="folder-art" role="img" aria-label="Large soft decorative letterform in blue tones"></div>
    <div class="brand brand--white"><span class="brand-mark"></span><span class="brand-name"><span class="line1">HOLLOWAY</span><span class="line2">ADVISORY PTY LTD</span></span></div>
  </div>

  <div class="piece letterhead" style="left:648px;top:400px">
    <div class="brand"><span class="brand-mark"></span><span class="brand-name"><span class="line1">HOLLOWAY</span><span class="line2">ADVISORY PTY LTD</span></span></div>
    <div class="letter-body">
      <p>May 30, 2024</p>
      <p>Marian Tolley<br>14 Garnet Street<br>Elmsford Park, Vic 3187</p>
      <p>Dear Ms. Tolley:</p>
      <p>Thank you for choosing our practice to look after your business accounts this year.</p>
      <p>We have reviewed the records you supplied and prepared a summary of your quarterly activity statements, along with a plan for the coming financial year. Your bookkeeping is in good order and only a few small items need your attention.</p>
      <p>Our team has also looked at your payroll and superannuation obligations. We recommend a short meeting to confirm your employee records and to discuss the new reporting dates that apply from next quarter.</p>
      <p>In addition, we can help you set a simple monthly budget and review your cash flow so that tax payments are planned well in advance.</p>
      <p>We would welcome the chance to meet with you and talk through your goals for the business. We look forward to hearing from you soon.</p>
      <p>Regards,</p>
      <p>Dana Whitfield</p>
    </div>
    <div class="footer-contact"><b>Tel :</b> 0417262938 | <b>Address :</b> PO Box 482, Elmsford Park, Vic 3187</div>
    <div class="footer-bar"></div>
  </div>
</section>

<section class="stage stage--cards" aria-label="Business card, back and front">
  <div class="piece card card--back" style="left:480px;top:70px">
    <div class="folder-art" role="img" aria-label="Large soft decorative letterform in blue tones"></div>
    <div class="brand brand--white"><span class="brand-mark"></span><span class="brand-name"><span class="line1">HOLLOWAY</span><span class="line2">ADVISORY PTY LTD</span></span></div>
  </div>

  <div class="piece card card--front" style="left:110px;top:450px">
    <div class="brand"><span class="brand-mark"></span><span class="brand-name"><span class="line1">HOLLOWAY</span><span class="line2">ADVISORY PTY LTD</span></span></div>
    <div class="card-person"><div class="card-name">Peter Lawson</div><div class="card-role">Manager</div></div>
    <div class="card-contact"><div><b>Tel :</b> 0417262938</div><div><b>Address :</b> PO Box 482, Elmsford Park, Vic 3187</div></div>
  </div>
</section>

</body>
</html>
```